Business Card for TLK Field Services

Would like a large logo on one side. On the other side, logo on one side and company phone number, address, and email on the other side. I don't have a logo so please create one for us.
Updates
I don't have a logo, so please create one for us.
Target Market(s)
Land Surveying
Industry/Entity Type
Surveyor
Contact Information for Business Card
Would like a large logo on one side. On the other side, logo on one side and company phone number, address, and email on the other side
Requirements
Nice to have
- would like the initials to be incorporated with the logo

```html
<!DOCTYPE html>
<html lang="en">
<head>
<meta charset="UTF-8">
<title>TLK Field Services – Business Card</title>
<link rel="stylesheet" href="https://fonts.googleapis.com/css2?family=Arimo:wght@400;700&display=swap">
<style>
  :root {
    --backdrop: #e4e4e2;
    --card-black: #1f1d1d;
    --card-white: #f1f1ef;
    --brand-yellow: #e8d81a;
    --card-shadow: 0 10px 28px rgba(0, 0, 0, 0.22);
  }
  * { box-sizing: border-box; margin: 0; padding: 0; }
  html, body {
    width: 1200px;
    height: 960px;
    overflow: hidden;
    background: var(--backdrop);
    font-family: "Arimo", Arial, sans-serif;
  }
  .canvas {
    width: 1200px;
    height: 960px;
    display: flex;
    flex-direction: column;
    align-items: center;
    justify-content: center;
    gap: 56px;
  }
  .card {
    width: 700px;
    height: 400px;
    box-shadow: var(--card-shadow);
    display: flex;
    overflow: hidden;
  }

  /* Back: large brand name */
  .card-back {
    background: var(--card-black);
    align-items: center;
    justify-content: center;
  }
  .brand {
    display: flex;
    align-items: center;
    gap: 16px;
    color: var(--brand-yellow);
    font-weight: 400;
  }
  .brand-dot {
    border-radius: 50%;
    background: var(--brand-yellow);
    flex: none;
  }
  .brand--large { font-size: 40px; }
  .brand--large .brand-dot { width: 30px; height: 30px; }
  .brand--small { font-size: 25px; gap: 10px; }
  .brand--small .brand-dot { width: 18px; height: 18px; }

  /* Front: brand panel + contact panel */
  .front-brand-panel {
    width: 46%;
    background: var(--card-white);
    display: flex;
    align-items: center;
    justify-content: center;
  }
  .front-contact-panel {
    width: 54%;
    background: var(--card-black);
    color: var(--brand-yellow);
    padding: 54px 30px 40px 40px;
    display: flex;
    flex-direction: column;
  }
  .person-name {
    font-size: 25px;
    font-weight: 700;
  }
  .person-title {
    font-size: 17px;
    margin-top: 6px;
  }
  .address {
    font-size: 17px;
    line-height: 1.3;
    margin-top: 62px;
    padding-left: 20px;
  }
  .contact-lines {
    list-style: none;
    font-size: 18px;
    line-height: 1.6;
    margin-top: 22px;
  }
</style>
</head>
<body>
  <main class="canvas">
    <section class="card card-back" aria-label="Business card back">
      <div class="brand brand--large">
        <span class="brand-dot"></span>
        <span class="brand-name">TLK Field Services</span>
      </div>
    </section>

    <section class="card card-front" aria-label="Business card front">
      <div class="front-brand-panel">
        <div class="brand brand--small">
          <span class="brand-dot"></span>
          <span class="brand-name">TLK Field Services</span>
        </div>
      </div>
      <div class="front-contact-panel">
        <p class="person-name">Your Name goes here</p>
        <p class="person-title">Your Title goes here</p>
        <p class="address">Your Address goes<br>here .....................</p>
        <ul class="contact-lines">
          <li>p: 0123456789</li>
          <li>e: yourname@tlkmail.com</li>
        </ul>
      </div>
    </section>
  </main>
</body>
</html>
```